Gift Card Design - Suds Harbor Co

I am needing a design for a standard plastic gift card, (ever so slightly large then a standard rounded edge business card). Name of the business is Suds Harbor Co. Attached is a file with a poor example, done by an equipment manufacturing firm, that I feel could be much better. Simple, clean and classy with what it is and does along with our name is what I am looking for. Attached also is out logo and source of logo, they don't have to be on the card.

Target Market(s)

Car wash customers in an upscale market.

Industry/Entity Type

Business

Font styles to use
Serif
Other font styles liked:
• whatever you feel, but I do like the font on a Brevanto golf ball

Requirements
Must have
• Words anywhere on the card -
• Reloadable Card
• Self Serve Bays & Vacuums.
• Also need name of the business, Suds Harbor Co.
Nice to have
• Work in Pantone #7483 as there is existing signage with that as a primary color, just trying to tie things together. Attached is my business logo and a picture of the source of the logo, you do not have to use those if you don't want to. I do like clean and classy but am open to creativity, that's why I am submitting this project.
Should not have
• Naked lady pictures

```html
<!DOCTYPE html>
<html lang="en">
<head>
<meta charset="utf-8">
<title>Suds Harbor Co — Reloadable Card</title>
<link href="https://fonts.googleapis.com/css2?family=Lustria&family=Questrial&family=Arimo:wght@700&display=swap" rel="stylesheet">
<style>
  :root {
    --backdrop: #000c0f;
    --harbor-teal: #037582;
    --deep-teal: #025f69;
    --card-white: #ffffff;
  }
  html, body {
    margin: 0;
    padding: 0;
    width: 1200px;
    height: 1200px;
    overflow: hidden;
    background: var(--backdrop);
  }
  .gift-card {
    position: absolute;
    left: 43px;
    top: 204px;
    width: 1133px;
    height: 680px;
    border-radius: 12px;
    overflow: hidden;
    background: var(--card-white);
  }
  .card-art {
    position: absolute;
    inset: 0;
    width: 100%;
    height: 100%;
  }
  .brand-name {
    position: absolute;
    left: 12px;
    top: 8px;
    margin: 0;
    font-family: "Lustria", Georgia, serif;
    font-weight: 400;
    font-size: 124px;
    line-height: 1;
    letter-spacing: -1px;
    color: var(--harbor-teal);
    white-space: nowrap;
  }
  .service-line {
    position: absolute;
    left: 22px;
    top: 190px;
    margin: 0;
    font-family: "Questrial", Arial, sans-serif;
    font-size: 35px;
    letter-spacing: 2.4px;
    color: var(--card-white);
    white-space: nowrap;
  }
  .reload-badge {
    position: absolute;
    right: 0;
    top: 594px;
    width: 490px;
    height: 68px;
    border-radius: 10px 0 0 10px;
    background: var(--deep-teal);
    display: flex;
    align-items: center;
    justify-content: flex-end;
    padding-right: 18px;
    box-sizing: border-box;
    font-family: "Arimo", Arial, sans-serif;
    font-weight: 700;
    font-size: 48px;
    letter-spacing: 1px;
    color: var(--card-white);
    white-space: nowrap;
  }
</style>
</head>
<body>
  <div class="gift-card">
    <svg class="card-art" viewBox="0 0 1133 680" xmlns="http://www.w3.org/2000/svg" aria-hidden="true">
      <path class="accent-line" d="M0 154 C 400 150, 850 148, 1133 172 L1133 180 C 850 158, 400 160, 0 163 Z" fill="#037582"/>
      <path class="teal-field" d="M0 178 C 400 175, 850 170, 1133 200 L1133 680 L0 680 Z" fill="#037582"/>
    </svg>
    <svg class="card-art" viewBox="0 0 1133 680" xmlns="http://www.w3.org/2000/svg" role="img" aria-label="Clock face illustration showing the time">
      <circle cx="102" cy="530" r="228" fill="#ffffff" fill-opacity="0.12"/>
    </svg>
    <h1 class="brand-name">Suds Harbor Co</h1>
    <p class="service-line">Self Serve Bays &amp; Vacuums</p>
    <div class="reload-badge">Reloadable Card</div>
  </div>
</body>
</html>
```